Business Card Design Project

Our organization is in need of a business card design with the use of our logo. We are looking for professional design that will embellish the image our consulting firm.

Here is a summary of what we do: Quorvent is systems consulting firm that specializes in the management, migration, and maintenance of IT infrastructure solutions.

Here is a link to my website: http://quorvent-example.com

I have attached the logo.

Target Market(s)

Organization that need IT and server support.

Industry/Entity Type

Business

```html
<!DOCTYPE html>
<html lang="en">
<head>
<meta charset="utf-8">
<title>Quorvent Business Card</title>
<link href="https://fonts.googleapis.com/css2?family=Montserrat:wght@600&family=Questrial&display=swap" rel="stylesheet">
<style>
  :root {
    --navy: #1d2a5c;
    --orange: #f26b1d;
    --white: #ffffff;
    --bubble: #e9e9e9;
    --stage: #3a3a3a;
    --ink-dark: #2c2c2c;
  }
  * { margin: 0; padding: 0; box-sizing: border-box; }
  html, body { width: 1200px; height: 900px; overflow: hidden; }
  body { background: var(--stage); position: relative; font-family: "Questrial", sans-serif; }

  .card {
    position: absolute; top: 292px; width: 520px; height: 316px;
    border-radius: 22px; overflow: hidden;
    box-shadow: 0 6px 14px rgba(0,0,0,.45);
  }
  .card--front { left: 70px; }
  .card--back { left: 610px; background: var(--white); }

  /* front */
  .front-photo {
    position: absolute; inset: 0;
    background: radial-gradient(ellipse at 50% 40%, #b5b5b5 0%, #9d9d9d 55%, #8a8a8a 100%);
  }
  .front-brand {
    position: absolute; left: 34px; top: 238px;
    display: flex; align-items: center; gap: 14px;
  }
  .brand-dot { width: 26px; height: 26px; border-radius: 50%; background: var(--navy); }
  .front-brand .brand-name { font-size: 30px; color: var(--navy); letter-spacing: .2px; }
  .front-tagline {
    position: absolute; right: 28px; top: 258px;
    font-size: 11.5px; letter-spacing: .4px; color: var(--ink-dark);
  }

  /* back */
  .back-texture {
    position: absolute; right: 0; top: 0; width: 150px; height: 140px;
    background: radial-gradient(ellipse at 80% 25%, var(--bubble) 0%, rgba(233,233,233,.6) 45%, rgba(255,255,255,0) 75%);
  }
  .back-art { position: absolute; inset: 0; }
  .back-brand {
    position: absolute; left: 82px; top: 50px;
    display: flex; align-items: center; gap: 26px;
  }
  .back-brand .brand-dot { width: 42px; height: 42px; }
  .back-brand .brand-name { font-size: 46px; color: var(--navy); }

  .holder { position: absolute; left: 42px; top: 192px; color: var(--white); }
  .holder-name { font-family: "Montserrat", sans-serif; font-weight: 600; font-size: 18px; color: var(--orange); }
  .holder-role { font-size: 15.5px; margin-top: 2px; }
  .holder-links { margin-top: 14px; }

  .contact-line {
    display: flex; align-items: center; gap: 6px;
    font-size: 12px; line-height: 18px; color: var(--white); white-space: nowrap;
  }
  .contact-line svg { width: 10px; height: 10px; flex: none; fill: var(--white); }
  .contact-line.indent { padding-left: 16px; }

  .divider {
    position: absolute; left: 285px; top: 198px; width: 1px; height: 80px;
    background: rgba(255,255,255,.5);
  }
  .contact-list { position: absolute; left: 300px; top: 194px; }
</style>
</head>
<body>

<section class="card card--front">
  <div class="front-photo" role="img" aria-label="Black-and-white vintage photo of two smiling men in cardigans and ties facing each other, one holding a trophy"></div>
  <div class="front-brand">
    <span class="brand-dot"></span>
    <span class="brand-name">quorvent</span>
  </div>
  <p class="front-tagline">SYSTEMS SOLUTIONS</p>
</section>

<section class="card card--back">
  <div class="back-texture" role="img" aria-label="Soft decorative cluster of pale grey circles"></div>
  <svg class="back-art" viewBox="0 0 520 316" width="520" height="316" aria-hidden="true">
    <path d="M0 150 C 120 162, 300 158, 520 130 L520 316 L0 316 Z" fill="var(--navy)"/>
    <path d="M70 157 C 220 162, 380 150, 520 126 L520 134 C 380 156, 220 165, 70 157 Z" fill="var(--orange)"/>
  </svg>

  <div class="back-brand">
    <span class="brand-dot"></span>
    <span class="brand-name">quorvent</span>
  </div>

  <div class="holder">
    <h1 class="holder-name">Martin Hollway</h1>
    <p class="holder-role">managing director</p>
    <div class="holder-links">
      <p class="contact-line">
        <svg viewBox="0 0 10 10"><path d="M0 2h10v6H0z M0 2l5 3.5L10 2" fill="var(--white)" stroke="var(--navy)" stroke-width=".8"/></svg>
        info@quorvent-example.com
      </p>
      <p class="contact-line">
        <svg viewBox="0 0 10 10"><circle cx="5" cy="5" r="4.4" fill="none" stroke="var(--white)" stroke-width="1.1"/><path d="M.6 5h8.8M5 .6v8.8" stroke="var(--white)" stroke-width=".9"/><ellipse cx="5" cy="5" rx="2" ry="4.4" fill="none" stroke="var(--white)" stroke-width=".9"/></svg>
        www.quorvent-example.com
      </p>
    </div>
  </div>

  <div class="divider"></div>

  <div class="contact-list">
    <p class="contact-line">
      <svg viewBox="0 0 10 10"><path d="M5 0a3.6 3.6 0 0 0-3.6 3.6C1.4 6.3 5 10 5 10s3.6-3.7 3.6-6.4A3.6 3.6 0 0 0 5 0zm0 5a1.4 1.4 0 1 1 0-2.8A1.4 1.4 0 0 1 5 5z"/></svg>
      4821 Meridian Loop
    </p>
    <p class="contact-line indent">Austin, TX 78745</p>
    <p class="contact-line">
      <svg viewBox="0 0 10 10"><circle cx="5" cy="5" r="4.4" fill="none" stroke="var(--white)" stroke-width=".9"/><path d="M3.2 2.6l1 1-.6.7c.4.8 1 1.4 1.8 1.8l.7-.6 1 1-.8.9C4.6 7.2 2.8 5.4 2.6 3.4z"/></svg>
      888 555 0142 (toll-free in US)
    </p>
    <p class="contact-line">
      <svg viewBox="0 0 10 10"><circle cx="5" cy="5" r="4.4" fill="none" stroke="var(--white)" stroke-width=".9"/><path d="M3.2 2.6l1 1-.6.7c.4.8 1 1.4 1.8 1.8l.7-.6 1 1-.8.9C4.6 7.2 2.8 5.4 2.6 3.4z"/></svg>
      512 555 0187 (local)
    </p>
    <p class="contact-line">
      <svg viewBox="0 0 10 10"><path d="M2.5 0h5v3h-5z M0 3.5h10v4H8V6H2v1.5H0z M2.5 6.5h5V10h-5z"/></svg>
      512 555 0188
    </p>
  </div>
</section>

</body>
</html>
```